Unique business card design

We are looking for a design that reflects our unique social media and online marketing agency "Kestrel Media". We are a young agency with a focus on speakers, coaches and trainers. In other words, we support people who want to do good with their work and help other people live a happier, more successful and fulfilling life, reach as many people as possible with their work and thus have an influence. Our values are: sustainability, creating added value, individuality, proactivity. We want our clients to feel comfortable with us and that's why the relationship with them is very important to us. We want every customer to become a lifelong friend of the company. Most of our clients are premium coaches, meaning they are in the higher priced segment and expect seriousness, professionalism and quality. All of these things should reflect our business card as well. I look forward to feedback. Best regards, Tomas Wylander

```html
<!DOCTYPE html>
<html lang="en">
<head>
<meta charset="utf-8">
<title>Kestrel Media – Business Card</title>
<link rel="stylesheet" href="https://fonts.googleapis.com/css2?family=Questrial&family=Raleway:wght@700&display=swap">
<style>
  :root {
    --navy: #24225e;
    --accent: #1b74bc;
    --accent-text: #2a7bc6;
    --white: #ffffff;
    --page: #ffffff;
    --shadow: rgba(0, 0, 0, 0.28);
  }
  * { box-sizing: border-box; margin: 0; padding: 0; }
  html, body { width: 1200px; height: 1200px; overflow: hidden; background: var(--page); }
  .canvas { position: relative; width: 1200px; height: 1200px; font-family: "Questrial", sans-serif; }

  .card {
    position: absolute;
    width: 393px;
    height: 682px;
    background: var(--navy);
    border-bottom: 3px solid var(--accent);
    box-shadow: 6px 8px 8px var(--shadow);
    color: var(--white);
  }
  .card--front { left: 186px; top: 233px; }
  .card--back { left: 672px; top: 339px; }

  .logo-plate {
    position: absolute;
    width: 188px;
    height: 105px;
    background: var(--white);
    display: flex;
    align-items: center;
    justify-content: center;
    gap: 8px;
  }
  .card--front .logo-plate { left: 100px; top: 143px; }
  .card--back .logo-plate { left: 102px; top: 143px; }
  .logo-square { width: 16px; height: 16px; background: var(--navy); }
  .logo-name { font-family: "Questrial", sans-serif; font-size: 21px; color: var(--navy); }

  .holder { position: absolute; left: 0; right: 0; top: 339px; text-align: center; }
  .holder-name { font-family: "Raleway", sans-serif; font-weight: 700; font-size: 25px; letter-spacing: 0.2px; }
  .holder-role { margin-top: 6px; font-size: 16.5px; color: var(--accent-text); }

  .contact {
    position: absolute;
    left: 50%;
    transform: translateX(-50%);
    height: 34px;
    background: var(--accent);
    display: flex;
    align-items: center;
    justify-content: center;
    gap: 8px;
    font-size: 17px;
    white-space: nowrap;
  }
  .contact--phone { top: 489px; width: 193px; }
  .contact--email { top: 539px; width: 232px; }
  .contact svg { flex: none; }

  .values { position: absolute; left: 99px; top: 384px; width: 194px; list-style: none; text-align: center; }
  .value { height: 34px; line-height: 34px; font-size: 19px; margin-bottom: 2px; }
  .value--boxed { background: var(--accent); }
</style>
</head>
<body>
<div class="canvas">

  <section class="card card--front">
    <div class="logo-plate">
      <span class="logo-square"></span>
      <span class="logo-name">Kestrel Media</span>
    </div>
    <div class="holder">
      <h1 class="holder-name">Tomas Wylander</h1>
      <p class="holder-role">Your Designation</p>
    </div>
    <div class="contact contact--phone">
      <svg width="17" height="17" viewBox="0 0 24 24" aria-hidden="true"><path fill="#1a2a5c" d="M6.6 10.8a15.1 15.1 0 0 0 6.6 6.6l2.2-2.2c.3-.3.7-.4 1-.2 1.1.4 2.3.6 3.6.6.6 0 1 .4 1 1V20c0 .6-.4 1-1 1A17 17 0 0 1 3 4c0-.6.4-1 1-1h3.5c.6 0 1 .4 1 1 0 1.3.2 2.5.6 3.6.1.3 0 .7-.2 1l-2.3 2.2z"/></svg>
      <span>123.456.7890</span>
    </div>
    <div class="contact contact--email">
      <svg width="22" height="16" viewBox="0 0 22 16" aria-hidden="true"><rect x="0" y="0" width="22" height="16" rx="1.5" fill="#1a2a5c"/><path d="M1.5 1.5 11 9l9.5-7.5" fill="none" stroke="#1b74bc" stroke-width="1.6"/></svg>
      <span>youremail@email.com</span>
    </div>
  </section>

  <section class="card card--back">
    <div class="logo-plate">
      <span class="logo-square"></span>
      <span class="logo-name">Kestrel Media</span>
    </div>
    <ul class="values">
      <li class="value value--boxed">Nachhaltigkeit</li>
      <li class="value">Mehrwert schaffen</li>
      <li class="value value--boxed">Individualität</li>
      <li class="value">Proaktivität</li>
    </ul>
  </section>

</div>
</body>
</html>
```